business card design for a small scale specialty cut flower farm

We need a business card design for Hollowmere Bloom Farm based in Alderwick Vale, Northmoor. We produce specialty, high-end cut flowers and sell locally to florists, local shops and markets and the end user through bouquet subscriptions. The final business card design should be memorable and have a timeless or vintage feel. We would prefer a square shape.
Updates

Target Market(s)

florists, shops and seasonal markets, local flower lovers

Industry/Entity Type

Floral

Contact Information for Business Card

Tamsin Ellery Voss, Grower
Alderwick Vale, Northmoor
website: hollowmerebloomfarm.example
instagram: @hollowmerebloomfarm
Tel: 555.317.4290
facebook: www.facebook.example/hollowmereblooms/

Font styles to use
Serif
Decorative
Script

Requirements
Must have
• soft black background colour on front side, the included logo and catch phrase: Fresh Local Seasonal
Nice to have
• phone number and website address on front of card, included photo 6539 incorporated onto the back, possibly photo 6609 as well.

```html
<!DOCTYPE html>
<html lang="en">
<head>
<meta charset="utf-8">
<title>Hollowmere Bloom Farm – Business Card</title>
<link rel="stylesheet" href="https://fonts.googleapis.com/css2?family=Lato:wght@400&family=Patrick+Hand&family=Parisienne&display=swap">
<style>
  :root {
    --page-bg: #e4e4e4;
    --soft-black: #4a4546;
    --white: #ffffff;
    --rose: #d98abd;
    --rose-band: #dd8fc0;
    --rose-dot: #e9a9cf;
    --ink: #2f2b2c;
    --muted: #d9d5d6;
    --panel: rgba(255, 255, 255, 0.72);
  }
  * { margin: 0; padding: 0; box-sizing: border-box; }
  html, body { width: 1200px; height: 960px; overflow: hidden; }
  body { background: var(--page-bg); position: relative; font-family: "Lato", sans-serif; }

  .card {
    position: absolute;
    top: 296px;
    width: 385px;
    height: 386px;
    overflow: hidden;
  }

  /* Front */
  .card-front {
    left: 192px;
    background: var(--soft-black);
    color: var(--white);
    text-align: center;
  }
  .brand-dot {
    position: absolute;
    left: 50%;
    top: 72px;
    width: 56px;
    height: 56px;
    margin-left: -28px;
    border-radius: 50%;
    background: var(--rose-dot);
  }
  .brand-name {
    position: absolute;
    left: 0; right: 0;
    top: 154px;
    font-family: "Lato", sans-serif;
    font-weight: 400;
    font-size: 34px;
    line-height: 44px;
    letter-spacing: 2px;
    color: var(--white);
  }
  .brand-tagline {
    position: absolute;
    left: 0; right: 0;
    top: 266px;
    font-family: "Parisienne", cursive;
    font-size: 17px;
    color: var(--muted);
  }
  .brand-est {
    position: absolute;
    left: 0; right: 0;
    top: 299px;
    font-size: 10px;
    letter-spacing: 3px;
    color: var(--muted);
  }
  .catchphrase {
    position: absolute;
    left: 0; right: 0;
    top: 326px;
    font-family: "Patrick Hand", cursive;
    font-size: 25px;
    line-height: 30px;
    letter-spacing: 0.5px;
    color: var(--rose);
  }

  /* Back */
  .card-back {
    left: 624px;
    background: #7fae5a;
  }
  .photo-area {
    position: absolute;
    inset: 0;
    background:
      radial-gradient(ellipse 45% 35% at 20% 8%, #f2f5ee 0%, rgba(242,245,238,0) 100%),
      radial-gradient(ellipse 60% 45% at 78% 22%, #8dbb5e 0%, rgba(141,187,94,0) 100%),
      linear-gradient(180deg, #cfdcc2 0%, #9cc474 35%, #6ea346 70%, #4f8a34 100%);
  }
  .name-band {
    position: absolute;
    left: 141px;
    top: 166px;
    width: 244px;
    height: 54px;
    background: var(--rose-band);
    color: var(--white);
    text-align: right;
    padding-right: 21px;
  }
  .person-name {
    font-family: "Patrick Hand", cursive;
    font-size: 25px;
    line-height: 26px;
    padding-top: 3px;
  }
  .person-role {
    font-size: 13px;
    line-height: 15px;
    letter-spacing: 0.5px;
    margin-top: 4px;
  }
  .contact-panel {
    position: absolute;
    left: 141px;
    top: 220px;
    width: 244px;
    height: 110px;
    background: var(--panel);
    padding: 7px 22px 0 0;
  }
  .contact-list { list-style: none; }
  .contact-item {
    display: flex;
    justify-content: flex-end;
    align-items: center;
    gap: 5px;
    font-size: 13.5px;
    line-height: 18px;
    color: var(--ink);
    white-space: nowrap;
  }
  .contact-item.location { margin-top: 6px; }
  .icon { width: 11px; height: 11px; flex: none; }
</style>
</head>
<body>

<section class="card card-front" aria-label="Card front">
  <div class="brand-dot" aria-hidden="true"></div>
  <h1 class="brand-name">Hollowmere<br>Bloom Farm</h1>
  <p class="brand-tagline">Specialty Cut Flowers</p>
  <p class="brand-est">EST.2019</p>
  <p class="catchphrase">Fresh Local Seasonal</p>
</section>

<section class="card card-back" aria-label="Card back">
  <div class="photo-area" role="img" aria-label="Photo of the grower standing among tall flowering plants in a sunny field"></div>

  <div class="name-band">
    <p class="person-name">Tamsin Ellery Voss</p>
    <p class="person-role">GROWER</p>
  </div>

  <div class="contact-panel">
    <ul class="contact-list">
      <li class="contact-item">(555) 317-4290
        <svg class="icon" viewBox="0 0 12 12" aria-hidden="true"><path d="M2.2 0.8 L4.2 0.8 L5 3.4 L3.8 4.4 C4.5 6 6 7.5 7.6 8.2 L8.6 7 L11.2 7.8 L11.2 9.8 C11.2 10.6 10.6 11.2 9.8 11.2 C5 11 1 7 0.8 2.2 C0.8 1.4 1.4 0.8 2.2 0.8 Z" fill="#2f2b2c"/></svg>
      </li>
      <li class="contact-item">hollowmerebloomfarm.example
        <svg class="icon" viewBox="0 0 12 12" aria-hidden="true"><circle cx="6" cy="6" r="5" fill="none" stroke="#2f2b2c" stroke-width="1.2"/><ellipse cx="6" cy="6" rx="2.2" ry="5" fill="none" stroke="#2f2b2c" stroke-width="1"/><line x1="1" y1="6" x2="11" y2="6" stroke="#2f2b2c" stroke-width="1"/></svg>
      </li>
      <li class="contact-item">@hollowmerebloomfarm
        <svg class="icon" viewBox="0 0 12 12" aria-hidden="true"><circle cx="6" cy="6" r="5.5" fill="#2f2b2c"/></svg>
      </li>
      <li class="contact-item">/hollowmereblooms
        <svg class="icon" viewBox="0 0 12 12" aria-hidden="true"><rect x="0.5" y="0.5" width="11" height="11" rx="1.5" fill="#2f2b2c"/></svg>
      </li>
      <li class="contact-item location">Alderwick Vale, Northmoor</li>
    </ul>
  </div>
</section>

</body>
</html>
```